Training Brochure for Local Government Program needs a makeover and some creative design!

We would like our plain and boring brochure updated to be enticing for people to register for this program. Our organisation works in Local Government (Councils) in Australia and we are running our "leadership" program again in 2017.

We would like the brochure for this program to be engaging, bright and modern to entice the future leaders to participate.

The original file was created in Publisher, however we require the final file to be an easily editable PDF with front and back cover for updating in future years and for minor content changes.

It is not intended that this will be printed but made available electronically, however A4 size would be appreciated.

We require the following to be included
Our Logo (Supplied)
KWEN Logo (To be supplied within 48 hours)

Target Market(s)

Aspiring Leaders in Government
Young business minded people

Industry/Entity Type

Government

Font styles to use
Serif
Sans Serif
Decorative

Colors

Designer to choose colors to be used in the design.

Requirements
Must have
• Our Logo - Supplied
• The Facilitators logo (KWEN) - Supplied
Nice to have
• Our Corporate colours used
• Some nice photo's or use of icons etc

```html
<!DOCTYPE html>
<html lang="en">
<head>
<meta charset="utf-8">
<title>Emerging Leaders Program – Application Form</title>
<link href="https://fonts.googleapis.com/css2?family=Arimo:wght@400;700&display=swap" rel="stylesheet">
<style>
  :root {
    --olive-band: #7d7c6b;
    --brand-green: #6c8f3b;
    --mint: #e2ebe5;
    --peach: #f3e5d8;
    --rule: #c9cfc2;
    --panel: #dfe6e0;
    --ink: #3a3a36;
    --white: #ffffff;
    --muted: #8b8b7c;
  }
  * { box-sizing: border-box; margin: 0; padding: 0; }
  html, body { width: 849px; height: 1200px; overflow: hidden; background: var(--white); }
  body { font-family: "Arimo", Arial, sans-serif; color: var(--ink); }
  .sheet { position: relative; width: 849px; height: 1200px; }

  .intro-band {
    position: absolute; left: 0; top: 0; width: 640px; height: 98px;
    background: var(--olive-band); color: var(--white);
    padding: 18px 34px 0 40px; font-size: 14px; line-height: 1.45;
  }
  .intro-band strong { font-weight: 700; }

  .org-mark {
    position: absolute; left: 662px; top: 36px; width: 170px;
    display: flex; align-items: center; gap: 10px;
    font-size: 14px; font-weight: 400; line-height: 1.3; color: var(--muted);
  }
  .org-mark .dot { flex: none; width: 30px; height: 30px; border-radius: 50%; border: 2px solid var(--muted); }

  .form-title {
    position: absolute; left: 0; width: 849px; top: 108px; text-align: center;
    font-size: 40px; font-weight: 700; color: var(--brand-green);
  }

  .field-label { position: absolute; left: 57px; font-size: 17px; }
  .field { position: absolute; left: 262px; width: 532px; height: 28px; }
  .field.mint { background: var(--mint); }
  .field.peach { background: var(--peach); }
  .field-block { position: absolute; left: 262px; width: 532px; }
  .field-block .line { height: 26px; border-bottom: 1px solid var(--rule); }

  .nomination-label { position: absolute; left: 57px; top: 826px; font-size: 16px; line-height: 1.15; }

  .support-band {
    position: absolute; left: 42px; top: 866px; width: 765px; height: 34px;
    background: var(--brand-green); color: var(--white);
    font-size: 18px; font-weight: 700; padding: 7px 14px;
  }
  .support-band small { font-size: 13px; font-weight: 400; }
  .support-panel { position: absolute; left: 42px; top: 900px; width: 765px; height: 210px; background: var(--panel); }

  .partner-mark {
    position: absolute; left: 42px; top: 1132px;
    display: flex; align-items: center; gap: 10px;
    font-size: 20px; font-weight: 400; color: var(--ink);
  }
  .partner-mark .dot { width: 20px; height: 20px; border-radius: 50%; background: var(--brand-green); }
</style>
</head>
<body>
<div class="sheet">
  <div class="intro-band">
    Civic Professionals Northland, in conjunction with KWEN (Institute for Regional Growth, Northland University), is pleased to offer the
    <strong>Emerging Leaders Program once again in 2017.</strong>
  </div>

  <div class="org-mark">
    <span class="dot"></span>
    <span>Civic Managers Network</span>
  </div>

  <h1 class="form-title">Application Form</h1>

  <span class="field-label" style="top:184px">Name:</span>
  <div class="field mint" style="top:180px"></div>

  <span class="field-label" style="top:218px">Position:</span>
  <div class="field peach" style="top:214px"></div>

  <span class="field-label" style="top:252px">Council/Organisation:</span>
  <div class="field mint" style="top:248px"></div>

  <span class="field-label" style="top:286px">Address:</span>
  <div class="field-block" style="top:282px; background:var(--peach)">
    <div class="line"></div><div class="line"></div><div class="line"></div><div class="line"></div><div class="line" style="border:0"></div>
  </div>

  <span class="field-label" style="top:436px">Telephone:</span>
  <div class="field mint" style="top:432px"></div>

  <span class="field-label" style="top:487px">Facsimile:</span>
  <div class="field peach" style="top:483px"></div>

  <span class="field-label" style="top:538px">Email:</span>
  <div class="field mint" style="top:534px"></div>

  <span class="field-label" style="top:586px">Date of Birth:</span>
  <div class="field peach" style="top:582px"></div>

  <span class="field-label" style="top:620px">Educational Qualifications:</span>
  <div class="field-block" style="top:616px; background:var(--mint)">
    <div class="line"></div><div class="line"></div><div class="line"></div><div class="line"></div>
    <div class="line"></div><div class="line"></div><div class="line"></div><div class="line" style="border:0"></div>
  </div>

  <span class="nomination-label">Nomination approved by:<br>GENERAL MANAGER</span>
  <div class="field peach" style="top:824px; height:32px"></div>

  <div class="support-band">Supporting Information to be Provided <small>(By Applicant)</small></div>
  <div class="support-panel"></div>

  <div class="partner-mark"><span class="dot"></span><span>KWEN</span></div>
</div>
</body>
</html>
```